Business Card Project for Firm Deck Hoisting

Business name is "Firm Deck Hoisting" we are a scaffolding & rigging business specialising in local and remote work for:
- scaffolding (residential, commercial, industrial)
- rigging
-man material hoists
- swing stages
- labour hire

On the back of the card I would like FDH as the symbol / logo. I have attached the logos we have had created by sketch harbour. We would like to use bold colours – preferably as the same colour scheme as the logo.

Target Market(s)

Construction business

Industry/Entity Type

Construction

Contact Information for Business Card

name: Owen Pellew
Title: Director
Phone: 0491 572 864
Address: PO BOX 3251, Marrowby SA 5190
Email: owen@firmdeckhoisting.com.au
Website: www.firmdeckhoisting.com.au

Font styles to use
Sans Serif

Requirements
Must have
• Must use existing logo & prefering using bold colours
Nice to have
• Would be nice to have a line of dot points in what we specialise in but not essential
• Would be nice to see some designs with a slogan but not essential
Should not have
• NA

```html
<!DOCTYPE html>
<html lang="en">
<head>
<meta charset="utf-8">
<title>Firm Deck Hoisting — Business Card</title>
<link rel="stylesheet" href="https://fonts.googleapis.com/css2?family=Jost:wght@400;500;600&display=swap">
<style>
  :root {
    --canvas: #e6e7e9;
    --brand-blue: #2f5fb6;
    --sky-blue: #5aa6dc;
    --paper: #f5f5f4;
    --mist-grey: #c9c9cb;
    --ink: #141414;
    --card-shadow: rgba(0, 0, 0, 0.18);
  }
  * { box-sizing: border-box; margin: 0; padding: 0; }
  html, body {
    width: 1200px; height: 870px; overflow: hidden;
    background: var(--canvas);
    font-family: "Jost", "Helvetica Neue", Arial, sans-serif;
    color: var(--ink);
  }
  .stage { position: relative; width: 1200px; height: 870px; }
  .card {
    position: absolute; width: 620px; height: 380px;
    background: var(--paper); overflow: hidden;
    box-shadow: 0 6px 18px var(--card-shadow);
  }
  .card-back { left: 470px; top: 45px; background: var(--brand-blue); }
  .card-front { left: 110px; top: 445px; }

  .accent-band { position: absolute; left: 0; right: 0; }
  .card-back .accent-band {
    top: 262px; bottom: 0;
    background: linear-gradient(180deg, var(--sky-blue) 0 14px, var(--paper) 14px 100%);
  }
  .card-front .accent-band {
    top: 312px; bottom: 0;
    background: linear-gradient(180deg, var(--mist-grey) 0 10px, var(--brand-blue) 10px 100%);
  }

  .wordmark { position: absolute; display: flex; align-items: center; gap: 14px; font-weight: 600; }
  .wordmark-initials { letter-spacing: 0.02em; }
  .wordmark-name { text-transform: uppercase; letter-spacing: 0.06em; }

  .card-back .wordmark { left: 0; right: 0; top: 108px; justify-content: center; color: var(--ink); }
  .card-back .wordmark-initials { font-size: 52px; }
  .card-back .wordmark-name { font-size: 26px; }

  .card-front .wordmark { left: 34px; top: 34px; color: var(--ink); }
  .card-front .wordmark-initials { font-size: 40px; }
  .card-front .wordmark-name { font-size: 20px; }

  .holder { position: absolute; left: 0; right: 0; top: 150px; text-align: center; }
  .holder-name { font-size: 28px; font-weight: 400; letter-spacing: 0.02em; text-transform: uppercase; }
  .holder-name strong { font-weight: 600; }
  .holder-title { font-size: 19px; margin-top: -2px; margin-left: 40px; }

  .contact-list { position: absolute; left: 40px; top: 228px; list-style: none; }
  .contact-item { display: flex; align-items: center; gap: 10px; height: 22px; font-size: 15px; }
  .contact-item.phone { font-size: 20px; height: 26px; }
  .contact-icon { width: 14px; height: 14px; flex: none; }

  .address {
    position: absolute; left: 40px; top: 342px;
    display: flex; align-items: center; gap: 10px;
    color: var(--paper); font-size: 15px;
  }
</style>
</head>
<body>
<main class="stage">

  <section class="card card-back" aria-label="Card back">
    <div class="accent-band" role="img" aria-label="Decorative colour band across the lower card"></div>
    <div class="wordmark">
      <span class="wordmark-initials">FDH</span>
      <span class="wordmark-name">Firm Deck Hoisting</span>
    </div>
  </section>

  <section class="card card-front" aria-label="Card front">
    <div class="accent-band" role="img" aria-label="Decorative colour band across the lower card"></div>

    <div class="wordmark">
      <span class="wordmark-initials">FDH</span>
      <span class="wordmark-name">Firm Deck Hoisting</span>
    </div>

    <div class="holder">
      <p class="holder-name"><strong>Owen</strong> Pellew</p>
      <p class="holder-title">Director</p>
    </div>

    <ul class="contact-list">
      <li class="contact-item phone">
        <svg class="contact-icon" viewBox="0 0 14 14" aria-hidden="true">
          <circle cx="7" cy="7" r="7" fill="var(--brand-blue)"/>
          <path d="M4.5,3.5 L6,3.5 L6.5,5.5 L5.6,6.2 C6,7.2 6.8,8 7.8,8.4 L8.5,7.5 L10.5,8 L10.5,9.5 C7,9.8 4.2,7 4.5,3.5 Z" fill="var(--paper)"/>
        </svg>
        0491 572 864
      </li>
      <li class="contact-item">
        <svg class="contact-icon" viewBox="0 0 14 14" aria-hidden="true">
          <circle cx="7" cy="7" r="7" fill="var(--brand-blue)"/>
          <rect x="3.5" y="4.5" width="7" height="5" fill="none" stroke="var(--paper)" stroke-width="1"/>
          <path d="M3.5,4.5 L7,7.3 L10.5,4.5" fill="none" stroke="var(--paper)" stroke-width="1"/>
        </svg>
        owen@firmdeckhoisting.com.au
      </li>
      <li class="contact-item">
        <svg class="contact-icon" viewBox="0 0 14 14" aria-hidden="true">
          <circle cx="7" cy="7" r="7" fill="var(--brand-blue)"/>
          <circle cx="7" cy="7" r="3.8" fill="none" stroke="var(--paper)" stroke-width="0.9"/>
          <path d="M3.2,7 L10.8,7 M7,3.2 C5,5 5,9 7,10.8 M7,3.2 C9,5 9,9 7,10.8" fill="none" stroke="var(--paper)" stroke-width="0.9"/>
        </svg>
        www.firmdeckhoisting.com.au
      </li>
    </ul>

    <p class="address">
      <svg class="contact-icon" viewBox="0 0 14 14" aria-hidden="true">
        <circle cx="7" cy="7" r="7" fill="var(--paper)"/>
        <path d="M7,11 C5,8.5 4.3,7.3 4.3,6 A2.7,2.7 0 0 1 9.7,6 C9.7,7.3 9,8.5 7,11 Z" fill="var(--brand-blue)"/>
        <circle cx="7" cy="6" r="1" fill="var(--paper)"/>
      </svg>
      PO BOX 3251, Marrowby SA 5190
    </p>
  </section>

</main>
</body>
</html>
```